2021 IT Training Presentation Deck Refresh

Copper Lantern is an IT education services firm. We teach IT industry standards and technologies. We are in need of an updated training presentation deck that factors in a fresh take for:

1) Agenda/Table of Contents
2) Chapter Topic Summary
2) Chapter Introduction and Learning Objectives
3) Chapter Recaps
4) Important Point/Pro Tip emphasis
5) Warning Message
6) Mini Quiz layout
7) Lab Exercise Introduction
7) Deck Close Out

Incorporating the official Copper Lantern colour palette for materials that will likely be used in self-paced/online recorded versions of courses.

Target Market(s)

IT

Industry/Entity Type

Computer Training

Requirements
Nice to have
• placeholder sections for images of IT workers in an office or by a computer

```html
<!DOCTYPE html>
<html lang="en">
<head>
<meta charset="utf-8">
<title>Copper Lantern – Training Deck Templates</title>
<link href="https://fonts.googleapis.com/css2?family=Montserrat:wght@400;500;600;700;800&family=Open+Sans:wght@400;600;700&display=swap" rel="stylesheet">
<style>
  :root{
    --brand-blue:#2b8ac6;
    --brand-blue-dark:#1f6fa8;
    --ink:#2d2d2d;
    --muted:#7a7a7a;
    --placeholder:#efefef;
    --panel:#ffffff;
    --stage:#ececec;
    --slate:#5b5b5b;
    --navy:#0f1e3a;
  }
  *{box-sizing:border-box;margin:0;padding:0}
  html,body{width:1200px;height:675px;overflow:hidden}
  body{position:relative;background:var(--stage);font-family:"Open Sans",sans-serif;color:var(--ink)}

  .sheet{position:absolute;left:0;top:0;width:429px;height:675px;background:var(--panel)}
  .showcase{position:absolute;left:429px;top:0;width:771px;height:675px;background:var(--stage)}

  .headline{position:absolute;font-family:"Montserrat",sans-serif;font-weight:800;color:#000;text-align:center;line-height:1.17}
  .headline--notice{left:0;width:771px;top:42px;font-size:19.5px}
  .headline--features{left:0;width:429px;top:590px;font-size:18.5px}

  .slide{position:absolute;width:188px;height:105px;background:var(--panel);overflow:hidden}
  .slide--large{transform:scale(1.1);transform-origin:top left;box-shadow:0 1px 3px rgba(0,0,0,.12)}
  .slide__title{position:absolute;left:0;width:188px;top:9px;text-align:center;font-family:"Montserrat",sans-serif;font-weight:500;font-size:7px;color:var(--ink)}
  .slide__dots{position:absolute;left:88px;top:19px;width:12px;height:2px;display:flex;justify-content:space-between}
  .slide__dots i{width:1.3px;height:1.3px;border-radius:50%;background:#b8c8d6}
  .slide__dots i:nth-child(2){background:var(--brand-blue)}
  .slide__brand{position:absolute;left:152px;top:7px;display:flex;flex-direction:column;align-items:center;gap:1px}
  .slide__brand-mark{width:7px;height:7px;border-radius:50%;background:var(--brand-blue)}
  .slide__brand-name{font-size:3px;color:var(--brand-blue);white-space:nowrap}
  .slide__nav{position:absolute;top:49px;width:8px;height:8px;background:var(--brand-blue);color:#fff;font-size:6px;line-height:8px;text-align:center;font-family:"Montserrat",sans-serif}
  .slide__nav--prev{left:0}
  .slide__nav--next{left:179px}
  .slide__nav--light{background:#fff;color:var(--ink)}
  .slide__footer{position:absolute;left:0;width:188px;bottom:4px;text-align:center;font-size:2.5px;color:#c4c4c4}
  .ph{position:absolute;background:var(--placeholder)}
  .body-text{position:absolute;font-size:3.2px;line-height:1.7;color:var(--muted)}
  .bullets{position:absolute;font-size:3.1px;line-height:2.1;color:var(--ink);list-style:none}
  .bullets li::before{content:"•";margin-right:3px}

  .slide--cover{background:var(--brand-blue)}
  .cover__title{position:absolute;left:0;width:188px;top:40px;text-align:center;font-family:"Montserrat",sans-serif;font-weight:600;font-size:19px;color:#fff}
  .cover__plus{position:absolute;color:#fff;font-size:7px;font-family:"Montserrat",sans-serif}
  .cover__rule{position:absolute;height:.4px;background:rgba(255,255,255,.35)}

  .btn{position:absolute;top:78px;height:7px;font-size:2.4px;color:#fff;line-height:7px;text-align:center}
  .agenda__label{position:absolute;font-size:2.2px;line-height:1.3;color:var(--muted);text-align:center;width:30px}
  .caption{position:absolute;font-size:3.2px;line-height:1.5;color:var(--muted);text-align:center}

  .quote__card{position:absolute;left:37px;top:44px;width:113px;height:32px;background:#fff;padding:7px 5px 0}
  .quote__text{font-size:3px;line-height:1.6;text-align:center}
  .quote__author{font-size:3px;text-align:right;margin-top:2px}

  .swot{position:absolute;width:60px;height:25px;color:#fff;text-align:center;padding-top:8px}
  .swot b{display:block;font-size:3.4px}
  .swot span{display:block;font-size:2.8px;margin-top:1px}
  .swot--blue{background:#3a8ec4}
  .swot--grey{background:var(--slate)}

  .step{position:absolute;font-size:2.6px;line-height:1.5;color:var(--muted);width:32px}
  .step b{display:block;color:var(--ink);font-size:3px}

  .band{position:absolute;left:34px;top:40px;width:120px;height:24px;background:rgba(40,40,40,.6);color:#fff;font-family:"Montserrat",sans-serif;font-weight:700;font-size:10px;text-align:center;line-height:24px}
  .band--chapter{background:rgba(55,65,75,.7)}

  .quiz__q{position:absolute;left:18px;top:25px;width:152px;font-size:3px;text-align:center}
  .quiz__choice{position:absolute;top:67px;width:44px;font-size:2.8px;color:var(--muted);text-align:center}
</style>
</head>
<body>

<section class="sheet">

  <div class="slide slide--cover" style="left:22px;top:22px">
    <span class="cover__plus" style="left:12px;top:6px">+</span>
    <span class="cover__plus" style="left:169px;top:88px">+</span>
    <span class="cover__rule" style="left:74px;top:15px;width:16px"></span>
    <span class="cover__rule" style="left:123px;top:8px;width:14px"></span>
    <span class="cover__rule" style="left:41px;top:46px;width:16px"></span>
    <span class="cover__rule" style="left:122px;top:98px;width:16px"></span>
    <div class="cover__title">Title</div>
  </div>

  <div class="slide" style="left:221px;top:22px">
    <div class="slide__title">WELCOME MESSAGE</div>
    <div class="slide__dots"><i></i><i></i><i></i></div>
    <div class="slide__brand"><span class="slide__brand-mark"></span><span class="slide__brand-name">Copper Lantern</span></div>
    <div class="ph" role="img" aria-label="Portrait of the course instructor" style="left:22px;top:29px;width:57px;height:57px;border-radius:50%"></div>
    <p class="body-text" style="left:88px;top:33px;width:78px;text-align:justify">Donec gravida leo porttitor maximus sagittis. Praesent non erat ligula. Curabitur nec turpis orci. Duis blandit ullamcorper purus, non accumsan lacus pharetra in. Vivamus enim quam. Morbi congue rutrum augue eu interdum. Donec vehicula.</p>
    <span class="btn" style="left:88px;width:22px;background:var(--brand-blue-dark)">More info</span>
    <span class="btn" style="left:110px;width:22px;background:var(--brand-blue)">Download</span>
    <span class="slide__nav slide__nav--prev">‹</span><span class="slide__nav slide__nav--next">›</span>
    <div class="slide__footer">© Copper Lantern</div>
  </div>

  <div class="slide" style="left:22px;top:136px">
    <div class="slide__title">AGENDA/TABLE OF CONTENTS</div>
    <div class="slide__dots"><i></i><i></i><i></i></div>
    <div class="slide__brand"><span class="slide__brand-mark"></span><span class="slide__brand-name">Copper Lantern</span></div>
    <svg width="188" height="105" style="position:absolute;left:0;top:0">
      <line x1="27" y1="60" x2="150" y2="60" stroke="#9ab8cf" stroke-width=".5"/>
      <g stroke="#9ab8cf" stroke-width=".5"><line x1="44" y1="60" x2="44" y2="68"/><line x1="66" y1="51" x2="66" y2="60"/><line x1="89" y1="60" x2="89" y2="68"/><line x1="111" y1="51" x2="111" y2="60"/><line x1="133" y1="60" x2="133" y2="68"/></g>
      <circle cx="27" cy="60" r="4" fill="#1f6fa8"/><circle cx="27" cy="59" r="1.1" fill="#fff"/><path d="M25 62 q2 -2 4 0" fill="#fff"/>
      <circle cx="150" cy="60" r="4" fill="#1f6fa8"/><path d="M148.5 62 v-4 l3 1 l-3 1" fill="none" stroke="#fff" stroke-width=".6"/>
      <g fill="#2b8ac6"><circle cx="44" cy="68" r="3.4"/><circle cx="66" cy="51" r="3.4"/><circle cx="89" cy="68" r="3.4"/><circle cx="111" cy="51" r="3.4"/><circle cx="133" cy="68" r="3.4"/></g>
      <g fill="#fff" font-family="Open Sans" font-size="3.4" font-weight="700" text-anchor="middle"><text x="44" y="69.2">1</text><text x="66" y="52.2">2</text><text x="89" y="69.2">3</text><text x="111" y="52.2">4</text><text x="133" y="69.2">5</text></g>
    </svg>
    <span class="agenda__label" style="left:29px;top:76px">PART 1<br>Content of part 1</span>
    <span class="agenda__label" style="left:51px;top:40px">PART 2<br>Content of part 2</span>
    <span class="agenda__label" style="left:74px;top:76px">PART 3<br>Content of part 3</span>
    <span class="agenda__label" style="left:96px;top:40px">PART 4<br>Content of part 4</span>
    <span class="agenda__label" style="left:118px;top:76px">PART 5<br>Content of part 5</span>
    <span class="slide__nav slide__nav--prev">‹</span><span class="slide__nav slide__nav--next">›</span>
    <div class="slide__footer">© Copper Lantern</div>
  </div>

  <div class="slide" style="left:221px;top:136px">
    <div class="slide__title">LAB EXERCISE INTRODUCTION</div>
    <div class="slide__dots"><i></i><i></i><i></i></div>
    <div class="slide__brand"><span class="slide__brand-mark"></span><span class="slide__brand-name">Copper Lantern</span></div>
    <div class="ph" role="img" aria-label="Photo of a calculator and computer mouse on a desk" style="left:22px;top:33px;width:71px;height:34px;background:linear-gradient(135deg,#e9eef2,#b9c3cb)"></div>
    <div class="ph" role="img" aria-label="Photo of a hand aiming a dart at a target beside a laptop" style="left:95px;top:33px;width:71px;height:34px;background:linear-gradient(135deg,#c9a68a,#6e6a66)"></div>
    <p class="caption" style="left:22px;top:76px;width:71px">Explanation and first step of what student have to do</p>
    <p class="caption" style="left:95px;top:76px;width:71px">Explanations and second step of what student have to do and how to do it</p>
    <span class="slide__nav slide__nav--prev">‹</span><span class="slide__nav slide__nav--next">›</span>
    <div class="slide__footer">© Copper Lantern</div>
  </div>

  <div class="slide" style="left:22px;top:250px">
    <div class="slide__title">PICTURES SLIDE</div>
    <div class="slide__dots"><i></i><i></i><i></i></div>
    <div class="slide__brand"><span class="slide__brand-mark"></span><span class="slide__brand-name">Copper Lantern</span></div>
    <div class="ph" role="img" aria-label="Photo of a business handshake in an office" style="left:18px;top:29px;width:151px;height:37px;background:linear-gradient(90deg,#8a7868,#c7bfb6 50%,#3f5a7a)"></div>
    <div class="ph" role="img" aria-label="Photo of IT workers reviewing documents at a desk" style="left:18px;top:68px;width:75px;height:24px;background:linear-gradient(135deg,#a9b5c2,#e4e1dc)"></div>
    <div style="position:absolute;left:95px;top:68px;width:74px;height:24px;background:var(--brand-blue-dark);color:#fff;font-size:3px;padding:7px 9px;line-height:1.6">Donec gravida leo portt itor maximus sagittis.</div>
    <span class="slide__nav slide__nav--prev">‹</span><span class="slide__nav slide__nav--next">›</span>
    <div class="slide__footer">© Copper Lantern</div>
  </div>

  <div class="slide" style="left:221px;top:250px">
    <div class="slide__title">CHAPTER LEARNING OBJECTIVES</div>
    <div class="slide__dots"><i></i><i></i><i></i></div>
    <div class="slide__brand"><span class="slide__brand-mark"></span><span class="slide__brand-name">Copper Lantern</span></div>
    <div class="ph" role="img" aria-label="Photo of an IT worker at a computer" style="left:18px;top:29px;width:49px;height:62px"></div>
    <ul class="bullets" style="left:72px;top:31px;width:96px">
      <li>Learning objective number 1</li>
      <li>Lorem ipsum dolor sit amet, consectetur</li>
      <li>adipiscing elit. Phasellus eros velit, imperdiet eget</li>
      <li>id, maximus in nunc. Sed lacinia tortor non metus</li>
      <li>Proin pharetra finibus metus,</li>
      <li>vitae porta sem vulputate a.</li>
    </ul>
    <span class="slide__nav slide__nav--prev">‹</span><span class="slide__nav slide__nav--next">›</span>
    <div class="slide__footer">© Copper Lantern</div>
  </div>

  <div class="slide" style="left:22px;top:363px">
    <div class="slide__title">CHAPTER RECAP</div>
    <div class="slide__dots"><i></i><i></i><i></i></div>
    <div class="slide__brand"><span class="slide__brand-mark"></span><span class="slide__brand-name">Copper Lantern</span></div>
    <ul class="bullets" style="left:22px;top:31px;width:56px;line-height:2.05">
      <li>1st point to recap of this chapter</li>
      <li>Lorem ipsum dolor sit amet, consectetur</li>
      <li>adipiscing elit. Phasellus eros velit, imperdiet eget scelerisque id, maximus in nunc. Sed lacinia tortor non metus finibus fermentum.</li>
      <li>Proin pharetra finibus metus,</li>
      <li>vitae porta sem vulputate a.</li>
    </ul>
    <svg width="188" height="105" style="position:absolute;left:0;top:0" role="img" aria-label="Photo area for the chapter topic"><polygon points="88,30 150,30 166,60 150,91 88,91" fill="#efefef"/></svg>
    <span class="slide__nav slide__nav--prev">‹</span><span class="slide__nav slide__nav--next">›</span>
    <div class="slide__footer">© Copper Lantern</div>
  </div>

  <div class="slide" style="left:221px;top:363px">
    <div class="slide__title">NICE QUOTE</div>
    <div class="slide__dots"><i></i><i></i><i></i></div>
    <div class="slide__brand"><span class="slide__brand-mark"></span><span class="slide__brand-name">Copper Lantern</span></div>
    <div class="ph" role="img" aria-label="Photo of a highway at dusk with motion blur" style="left:22px;top:29px;width:143px;height:62px;background:linear-gradient(180deg,#1b5fd0,#3c7fe0 40%,#2a3e6a 75%,#1d2a4a)"></div>
    <div class="quote__card">
      <p class="quote__text">"Tell me and I forget, teach me and I may remember, involve me and I learn."</p>
      <p class="quote__author">Marta Ellison</p>
    </div>
    <span class="slide__nav slide__nav--prev">‹</span><span class="slide__nav slide__nav--next">›</span>
    <div class="slide__footer">© Copper Lantern</div>
  </div>

  <div class="slide" style="left:22px;top:477px">
    <div class="slide__title">SOME GRAPH LIKE A SWOT</div>
    <div class="slide__dots"><i></i><i></i><i></i></div>
    <div class="slide__brand"><span class="slide__brand-mark"></span><span class="slide__brand-name">Copper Lantern</span></div>
    <span style="position:absolute;left:94px;top:28px;width:.5px;height:64px;background:#ccc"></span>
    <span style="position:absolute;left:28px;top:60px;width:132px;height:.5px;background:#ccc"></span>
    <div class="swot swot--blue" style="left:29px;top:30px"><b>1st part</b><span>• Donec gravida leo portt</span></div>
    <div class="swot swot--grey" style="left:98px;top:30px"><b>2nd part</b><span>• Donec gravida leo portt</span></div>
    <div class="swot swot--grey" style="left:29px;top:64px"><b>3rd part</b><span>• Donec gravida leo portt</span></div>
    <div class="swot swot--blue" style="left:98px;top:64px"><b>4th part</b><span>• Donec gravida leo portt</span></div>
    <span class="slide__nav slide__nav--prev">‹</span><span class="slide__nav slide__nav--next">›</span>
    <div class="slide__footer">© Copper Lantern</div>
  </div>

  <div class="slide" style="left:221px;top:477px">
    <div class="slide__title">IMPORTANT POINTS</div>
    <div class="slide__dots"><i></i><i></i><i></i></div>
    <div class="slide__brand"><span class="slide__brand-mark"></span><span class="slide__brand-name">Copper Lantern</span></div>
    <p class="body-text" style="left:18px;top:34px;width:48px;line-height:1.5">First important point out of three</p>
    <div class="ph" role="img" aria-label="Photo for the first point" style="left:69px;top:28px;width:49px;height:28px"></div>
    <p class="body-text" style="left:124px;top:34px;width:46px;line-height:1.5">Third important point out of three</p>
    <div class="ph" role="img" aria-label="Photo for the second point" style="left:18px;top:60px;width:49px;height:28px"></div>
    <p class="body-text" style="left:75px;top:67px;width:42px;line-height:1.5">Second important point out of three</p>
    <div class="ph" role="img" aria-label="Photo for the third point" style="left:120px;top:60px;width:49px;height:28px"></div>
    <span class="slide__nav slide__nav--prev">‹</span><span class="slide__nav slide__nav--next">›</span>
    <div class="slide__footer">© Copper Lantern</div>
  </div>

  <h2 class="headline headline--features">Fully customizable slide deck<br>All grey zones are for pictures upload<br>20+ different set up included</h2>
</section>

<section class="showcase">
  <h2 class="headline headline--notice">All pictures are for<br>illustration purpose<br>only</h2>

  <!-- Row 1 -->
  <div class="slide slide--large" style="left:55px;top:140px">
    <div class="slide__title">EXERCISE INTRODUCTION</div>
    <div class="slide__dots"><i></i><i></i><i></i></div>
    <div class="slide__brand"><span class="slide__brand-mark"></span><span class="slide__brand-name">Copper Lantern</span></div>
    <div class="ph" role="img" aria-label="Photo of a calculator and computer mouse on a desk" style="left:22px;top:33px;width:71px;height:34px;background:linear-gradient(135deg,#e9eef2,#b9c3cb)"></div>
    <div class="ph" role="img" aria-label="Photo of a hand aiming a dart at a target beside a laptop" style="left:95px;top:33px;width:71px;height:34px;background:linear-gradient(135deg,#c9a68a,#6e6a66)"></div>
    <p class="caption" style="left:22px;top:76px;width:71px">Explanation and first step of what student have to do</p>
    <p class="caption" style="left:95px;top:76px;width:71px">Explanations and second step of what student have to do and how to do it</p>
    <span class="slide__nav slide__nav--prev">‹</span><span class="slide__nav slide__nav--next">›</span>
    <div class="slide__footer">© Copper Lantern</div>
  </div>

  <div class="slide slide--large" style="left:282px;top:140px">
    <div class="slide__title">PROCESS SLIDE</div>
    <div class="slide__dots"><i></i><i></i><i></i></div>
    <div class="slide__brand"><span class="slide__brand-mark"></span><span class="slide__brand-name">Copper Lantern</span></div>
    <svg width="188" height="105" style="position:absolute;left:0;top:0">
      <circle cx="94" cy="60" r="22" fill="none" stroke="#2b8ac6" stroke-width="13"/>
      <g stroke="#fff" stroke-width="1"><line x1="94" y1="31" x2="94" y2="42"/><line x1="94" y1="78" x2="94" y2="89"/><line x1="65" y1="60" x2="76" y2="60"/><line x1="112" y1="60" x2="123" y2="60"/></g>
      <g fill="#fff"><circle cx="79" cy="45" r="4"/><circle cx="109" cy="45" r="4"/><circle cx="79" cy="75" r="4"/><circle cx="109" cy="75" r="4"/></g>
      <g fill="#2b8ac6" font-family="Open Sans" font-size="4" font-weight="700" text-anchor="middle"><text x="79" y="46.5">1</text><text x="109" y="46.5">2</text><text x="109" y="76.5">3</text><text x="79" y="76.5">4</text></g>
    </svg>
    <div class="step" style="left:26px;top:36px"><b>Step 01</b>Lorem ipsum dolor sit amet, consectetur</div>
    <div class="step" style="left:134px;top:36px"><b>Step 02</b>Lorem ipsum dolor sit amet, consectetur</div>
    <div class="step" style="left:134px;top:70px"><b>Step 03</b>Lorem ipsum dolor sit amet, consectetur</div>
    <div class="step" style="left:26px;top:70px"><b>Step 04</b>Lorem ipsum dolor sit amet, consectetur</div>
    <span class="slide__nav slide__nav--prev">‹</span><span class="slide__nav slide__nav--next">›</span>
    <div class="slide__footer">© Copper Lantern</div>
  </div>

  <div class="slide slide--large" style="left:509px;top:140px">
    <div class="slide__title">PC MOCKUP</div>
    <div class="slide__dots"><i></i><i></i><i></i></div>
    <div class="slide__brand"><span class="slide__brand-mark"></span><span class="slide__brand-name">Copper Lantern</span></div>
    <p class="caption" style="left:30px;top:24px;width:128px">Illustration of some PC/laptop screenshot if needed</p>
    <div style="position:absolute;left:50px;top:36px;width:88px;height:52px;border:3px solid #111;border-radius:3px;background:#f7f7f7"></div>
    <div style="position:absolute;left:42px;top:88px;width:104px;height:3px;background:#222;border-radius:0 0 3px 3px"></div>
    <span class="slide__nav slide__nav--prev">‹</span><span class="slide__nav slide__nav--next">›</span>
    <div class="slide__footer">© Copper Lantern</div>
  </div>

  <!-- Row 2 -->
  <div class="slide slide--large slide--cover" style="left:55px;top:268px">
    <span class="cover__plus" style="left:12px;top:6px">+</span>
    <span class="cover__plus" style="left:169px;top:88px">+</span>
    <span class="cover__rule" style="left:74px;top:15px;width:16px"></span>
    <span class="cover__rule" style="left:41px;top:46px;width:16px"></span>
    <span class="cover__rule" style="left:122px;top:98px;width:16px"></span>
    <div class="cover__title">Title</div>
  </div>

  <div class="slide slide--large" style="left:282px;top:268px">
    <div class="slide__title">CHAPTER LEARNING OBJECTIVES</div>
    <div class="slide__dots"><i></i><i></i><i></i></div>
    <div class="slide__brand"><span class="slide__brand-mark"></span><span class="slide__brand-name">Copper Lantern</span></div>
    <div class="ph" role="img" aria-label="Photo of an IT worker typing at a laptop" style="left:18px;top:29px;width:49px;height:62px;background:linear-gradient(135deg,#c99a6a,#e8e2da 50%,#4f6f95)"></div>
    <ul class="bullets" style="left:72px;top:31px;width:96px">
      <li>Learning objective number 1</li>
      <li>Lorem ipsum dolor sit amet, consectetur</li>
      <li>adipiscing elit. Phasellus eros velit, imperdiet eget</li>
      <li>id, maximus in nunc. Sed lacinia tortor non metus</li>
      <li>Proin pharetra finibus metus,</li>
      <li>vitae porta sem vulputate a.</li>
    </ul>
    <span class="slide__nav slide__nav--prev">‹</span><span class="slide__nav slide__nav--next">›</span>
    <div class="slide__footer">© Copper Lantern</div>
  </div>

  <div class="slide slide--large" style="left:509px;top:268px">
    <div class="slide__title">MINI QUIZ LAYOUT</div>
    <div class="slide__dots"><i></i><i></i><i></i></div>
    <div class="slide__brand"><span class="slide__brand-mark"></span><span class="slide__brand-name">Copper Lantern</span></div>
    <p class="quiz__q">Question of the mini quiz, example: pick the correct choice among the three below:</p>
    <div class="ph" role="img" aria-label="Picture for the first answer choice" style="left:22px;top:33px;width:44px;height:32px;background:linear-gradient(135deg,#2f9e4a,#e9cf3a)"></div>
    <div class="ph" role="img" aria-label="Picture for the second answer choice" style="left:72px;top:33px;width:44px;height:32px;background:linear-gradient(135deg,#2a2a3a,#6b5e9a)"></div>
    <div class="ph" role="img" aria-label="Picture for the third answer choice" style="left:122px;top:33px;width:44px;height:32px;background:linear-gradient(135deg,#1f6c6a,#3a9a92)"></div>
    <p class="quiz__choice" style="left:22px">First choice of answer proposal</p>
    <p class="quiz__choice" style="left:72px">Second choice of answer proposal</p>
    <p class="quiz__choice" style="left:122px">Third choice of answer proposal</p>
    <span class="slide__nav slide__nav--prev">‹</span><span class="slide__nav slide__nav--next">›</span>
    <div class="slide__footer">© Copper Lantern</div>
  </div>

  <!-- Row 3 -->
  <div class="slide slide--large" style="left:55px;top:396px;background:linear-gradient(135deg,#3a2a20,#8a6a4e 45%,#c8a885 60%,#4a3526)" role="img" aria-label="Photo of two hands holding cups of coffee">
    <div class="band">BREAK SLIDE</div>
    <span class="slide__nav slide__nav--prev slide__nav--light">‹</span><span class="slide__nav slide__nav--next slide__nav--light">›</span>
  </div>

  <div class="slide slide--large" style="left:282px;top:396px">
    <div class="slide__title">AGENDA/TABLE OF CONTENTS</div>
    <div class="slide__dots"><i></i><i></i><i></i></div>
    <div class="slide__brand"><span class="slide__brand-mark"></span><span class="slide__brand-name">Copper Lantern</span></div>
    <svg width="188" height="105" style="position:absolute;left:0;top:0">
      <line x1="27" y1="60" x2="150" y2="60" stroke="#9ab8cf" stroke-width=".5"/>
      <g stroke="#9ab8cf" stroke-width=".5"><line x1="44" y1="60" x2="44" y2="68"/><line x1="66" y1="51" x2="66" y2="60"/><line x1="89" y1="60" x2="89" y2="68"/><line x1="111" y1="51" x2="111" y2="60"/><line x1="133" y1="60" x2="133" y2="68"/></g>
      <circle cx="27" cy="60" r="4" fill="#1f6fa8"/><circle cx="27" cy="59" r="1.1" fill="#fff"/><path d="M25 62 q2 -2 4 0" fill="#fff"/>
      <circle cx="150" cy="60" r="4" fill="#1f6fa8"/><path d="M148.5 62 v-4 l3 1 l-3 1" fill="none" stroke="#fff" stroke-width=".6"/>
      <g fill="#2b8ac6"><circle cx="44" cy="68" r="3.4"/><circle cx="66" cy="51" r="3.4"/><circle cx="89" cy="68" r="3.4"/><circle cx="111" cy="51" r="3.4"/><circle cx="133" cy="68" r="3.4"/></g>
      <g fill="#fff" font-family="Open Sans" font-size="3.4" font-weight="700" text-anchor="middle"><text x="44" y="69.2">1</text><text x="66" y="52.2">2</text><text x="89" y="69.2">3</text><text x="111" y="52.2">4</text><text x="133" y="69.2">5</text></g>
    </svg>
    <span class="agenda__label" style="left:29px;top:76px">PART 1<br>Content of part 1</span>
    <span class="agenda__label" style="left:51px;top:40px">PART 2<br>Content of part 2</span>
    <span class="agenda__label" style="left:74px;top:76px">PART 3<br>Content of part 3</span>
    <span class="agenda__label" style="left:96px;top:40px">PART 4<br>Content of part 4</span>
    <span class="agenda__label" style="left:118px;top:76px">PART 5<br>Content of part 5</span>
    <span class="slide__nav slide__nav--prev">‹</span><span class="slide__nav slide__nav--next">›</span>
    <div class="slide__footer">© Copper Lantern</div>
  </div>

  <div class="slide slide--large" style="left:509px;top:396px">
    <div class="slide__title">CHAPTER RECAP</div>
    <div class="slide__dots"><i></i><i></i><i></i></div>
    <div class="slide__brand"><span class="slide__brand-mark"></span><span class="slide__brand-name">Copper Lantern</span></div>
    <ul class="bullets" style="left:22px;top:31px;width:56px;line-height:2.05">
      <li>1st point to recap of this chapter</li>
      <li>Lorem ipsum dolor sit amet, consectetur</li>
      <li>adipiscing elit. Phasellus eros velit, imperdiet eget scelerisque id, maximus in nunc. Sed lacinia tortor non metus finibus fermentum.</li>
      <li>Proin pharetra finibus metus,</li>
      <li>vitae porta sem vulputate a.</li>
    </ul>
    <svg width="188" height="105" style="position:absolute;left:0;top:0" role="img" aria-label="Photo of solar panels under a blue sky">
      <defs><linearGradient id="solar" x1="0" y1="0" x2="1" y2="1"><stop offset="0" stop-color="#8fb8e0"/><stop offset=".55" stop-color="#2e4f7c"/><stop offset="1" stop-color="#c9c3b8"/></linearGradient></defs>
      <polygon points="88,30 150,30 166,60 150,91 88,91" fill="url(#solar)"/>
    </svg>
    <span class="slide__nav slide__nav--prev">‹</span><span class="slide__nav slide__nav--next">›</span>
    <div class="slide__footer">© Copper Lantern</div>
  </div>

  <!-- Row 4 -->
  <div class="slide slide--large" style="left:55px;top:524px">
    <div class="slide__title">WARNING MESSAGE</div>
    <div class="slide__dots"><i></i><i></i><i></i></div>
    <div class="slide__brand"><span class="slide__brand-mark"></span><span class="slide__brand-name">Copper Lantern</span></div>
    <div class="ph" role="img" aria-label="Photo of a yellow caution sign on a floor" style="left:22px;top:30px;width:60px;height:60px;background:linear-gradient(135deg,#f0c020,#d89a10 60%,#c9b79a)"></div>
    <p style="position:absolute;left:92px;top:32px;font-size:3.6px;font-weight:700">Warning subtitle</p>
    <p class="body-text" style="left:92px;top:40px;width:76px;line-height:1.6">Duis nostrud exercitation ullamco laboris nisi ut aliquip ex ea commodo consequat. Duis aute irure dolor in reprehenderit in voluptate velit esse.</p>
    <span class="slide__nav slide__nav--prev">‹</span><span class="slide__nav slide__nav--next">›</span>
    <div class="slide__footer">© Copper Lantern</div>
  </div>

  <div class="slide slide--large" style="left:282px;top:524px;background:radial-gradient(circle at 55% 45%,#2a3f66,#0f1e3a 70%)" role="img" aria-label="Dark blue technology network background">
    <div class="band band--chapter">CHAPTER TITLE</div>
  </div>

  <div class="slide slide--large" style="left:509px;top:524px">
    <div class="slide__title">WELCOME MESSAGE</div>
    <div class="slide__dots"><i></i><i></i><i></i></div>
    <div class="slide__brand"><span class="slide__brand-mark"></span><span class="slide__brand-name">Copper Lantern</span></div>
    <div class="ph" role="img" aria-label="Portrait photo of the course instructor" style="left:22px;top:29px;width:57px;height:57px;border-radius:50%;background:linear-gradient(135deg,#d8d8d8,#9a9a9a)"></div>
    <p class="body-text" style="left:88px;top:33px;width:78px;text-align:justify">About me: some quick text to introduce the facilitator. Vivamus aliquet nisi sed pellentesque ultrices. Donec bibendum in justo eget imperdiet. Risus vel feugiat porttitor, sem eget vehicula.</p>
    <span class="btn" style="left:88px;width:22px;background:var(--brand-blue-dark)">More info</span>
    <span class="slide__nav slide__nav--prev">‹</span><span class="slide__nav slide__nav--next">›</span>
    <div class="slide__footer">© Copper Lantern</div>
  </div>
</section>

</body>
</html>
```